Meadowbrook Fellowship Chapel Banner Design

Designing 6 banners (3 + 3 that will hang on opposite sides of our auditorium) that are 10 feet long by 4 feet wide.

Use our branding guide - specifically item 4 (vertical logo) and item 5 (icon logo).

Design elements found in our AWAKE booklet, we would like to see designs that utilize the white, green and blue colour palettes but NOT the grey. Other colours may be incorporated (e.g. coral).

We are looking for 3 banner designs that would match on either side of the auditorium, the first banner incorporating the word "TRUTH", the second incorporating the word "LOVE", and the third incorporating the word "MISSION".

We interested in incorporating graphics such as trees or outdoor themes.

Font styles to use
Other font styles liked:
• Montserrat

Colors
34a7d7
00a990
f47c35

Requirements
Must have
• Banner Type #1 include the word "TRUTH"
Banner Type #2 include the word "LOVE"
Banner Type #3 include the word "MISSION"

Colour scheme must include CMYK 54 / 5 / 16 / 0 (which is available in the branding guide.) We have selected the three colours, included below in the brief.

From the branding guide - utilize #5 (icon) for the banner.

UPDATE: After reviewing the initial submissions, we are asking for designs that ONLY incorporate #5 - the ICON logo for the banners.
Nice to have
• It would be nice to have some creativity with the colour ... though a more minimalistic style is preferred.

Graphic adaptations such as trees in the background would be of interest.
Should not have
• Colour scheme should not be gray scale.

The banners should NOT be too busy.

Scripture verses (written out) are not necessary.

```html
<!DOCTYPE html>
<html lang="en">
<head>
<meta charset="utf-8">
<title>Meadowbrook Fellowship Chapel – Truth Banner</title>
<link rel="stylesheet" href="https://fonts.googleapis.com/css2?family=Montserrat:wght@700;800&family=Roboto+Slab:wght@700&family=Yellowtail&display=swap">
<style>
  :root {
    --banner-coral: #ee914a;
    --banner-white: #ffffff;
    --script-ink: #4a4650;
  }
  html, body {
    margin: 0;
    padding: 0;
    width: 1200px;
    height: 2780px;
    overflow: hidden;
  }
  .banner {
    position: relative;
    width: 1200px;
    height: 2780px;
    background: var(--banner-coral);
    color: var(--banner-white);
    overflow: hidden;
  }
  .statement {
    position: absolute;
    left: 0;
    width: 100%;
    margin: 0;
    text-align: center;
    line-height: 1;
  }
  .statement-i {
    top: 386px;
    font-family: "Roboto Slab", serif;
    font-weight: 700;
    font-size: 460px;
  }
  .statement-am {
    top: 876px;
    font-family: "Montserrat", sans-serif;
    font-weight: 800;
    font-size: 290px;
    letter-spacing: 8px;
  }
  .statement-the {
    top: 1108px;
    left: -20px;
    font-family: "Yellowtail", "Brush Script MT", cursive;
    font-style: italic;
    font-size: 120px;
    color: var(--script-ink);
    z-index: 2;
  }
  .statement-truth {
    top: 1200px;
    font-family: "Montserrat", sans-serif;
    font-weight: 700;
    font-size: 325px;
    letter-spacing: -4px;
    z-index: 1;
  }
  .church-mark {
    position: absolute;
    top: 1900px;
    left: 50%;
    transform: translateX(-50%);
    width: 440px;
    height: 440px;
  }
  .church-name {
    position: absolute;
    top: 2420px;
    left: 0;
    width: 100%;
    margin: 0;
    text-align: center;
    font-family: "Montserrat", sans-serif;
    font-weight: 700;
    font-size: 70px;
    line-height: 1.15;
    letter-spacing: 2px;
    text-transform: uppercase;
  }
  .church-name span { display: block; }
</style>
</head>
<body>
  <main class="banner">
    <p class="statement statement-i">I</p>
    <p class="statement statement-am">AM</p>
    <p class="statement statement-truth">truth</p>
    <p class="statement statement-the">the</p>

    <svg class="church-mark" viewBox="0 0 440 440" aria-hidden="true">
      <circle cx="220" cy="220" r="200" fill="none" stroke="var(--banner-white)" stroke-width="26"/>
    </svg>

    <p class="church-name">
      <span>Meadowbrook</span>
      <span>Fellowship Chapel</span>
    </p>
  </main>
</body>
</html>
```